Minimalistic logo and website for plovrak.com

My colleague and I just started a new company. We need a website to replace the placeholder at https://plovrak.com/

We need a onepager website. A logotype and color profiles. We like minimalism. Scandinavian design.

Below is just information about the company. You can rearrange it, add photos, emit stuff. Maybe even add stuff if you think it is necessary.

# About Plovrak
Plovrak builds critical applications to capture new markets, create modern services and captivate our customers in new and engaging ways. Creating effective and engaging solutions that truly work has always been Plovrak's core offering and is what makes us excited to work in digital. We are a forward thinking company embracing the opportunities of digital transformation and automations.

# Core services
Business automation
Application development and services for desktop and mobile
Interface Design and UX
Enterprise integrations

# Some more data
Plovrak was founded by Torvald Bergqvist and Mikael Dahlgren in 2021.
NetLinkPro: https://www.netlinkpro.example/company/74819203/admin/

# Inspiration
Minimal. Simple.
https://www.brunvikformstudio.se/contact

Target Market(s)

Businesses

Industry/Entity Type

IT, business automation, data

Number of Pages Required

1 page

Font styles to use
Sans Serif

Colors

Designer to choose colors to be used in the design.

Requirements
Must have
• Onepage design. Minimalism.
Should not have
• Menus

```html
<!DOCTYPE html>
<html lang="en">
<head>
<meta charset="utf-8">
<title>Plovrak</title>
<link rel="stylesheet" href="https://fonts.googleapis.com/css2?family=Poppins:wght@300;400;600&display=swap">
<style>
:root{
  --ink:#111111;
  --paper:#ffffff;
  --rule:#e2e2e2;
  --dark:#1c1c1c;
  --black:#000000;
  --muted:#d9d9d9;
}
*{margin:0;padding:0;box-sizing:border-box}
html,body{width:1200px;height:2851px;overflow:hidden}
body{font-family:'Poppins',sans-serif;color:var(--ink);background:var(--paper);position:relative;font-weight:400}
.abs{position:absolute}
.brand{font-weight:600;font-size:17px;letter-spacing:.2px}
.rule{position:absolute;left:37px;width:1126px;height:1px;background:var(--rule)}
.headline{left:37px;top:94px;width:760px;font-size:33px;line-height:37.5px;font-weight:400}
.side-social{left:1114px;top:97px;font-size:10px;line-height:28px}
.photo{position:absolute}
.hero-wide{left:37px;top:307px;width:1126px;height:469px;background:linear-gradient(120deg,#d8d4cc 0%,#b9a898 35%,#7a5a4a 60%,#cfcac4 100%)}
.hero-low{left:37px;top:775px;width:433px;height:100px;background:linear-gradient(90deg,#c9c3bb,#8a7868)}
.intro{left:550px;top:824px;width:510px;font-size:10px;line-height:19px}
.section-title{position:absolute;left:37px;font-size:40px;font-weight:400;line-height:1.2}
.services{left:550px;top:962px;list-style:none;font-size:16.5px;line-height:25px}
.services li{position:relative;padding-left:35px;margin-bottom:25px;width:400px}
.services li::before{content:"+";position:absolute;left:0;top:0;font-weight:600}
.founders{left:550px;top:1296px;font-size:16.5px}
.year{left:550px;top:1320px;font-size:13px}
.year b{font-weight:400;font-size:38px;margin-left:6px;vertical-align:-14px}
.connect{left:551px;top:1496px;font-size:16.5px;line-height:25px}
.proj-tall{left:998px;top:1702px;width:165px;height:418px;background:linear-gradient(160deg,#5a2de0,#8b3cf0 55%,#b06cf6)}
.proj-a{left:37px;top:1873px;width:433px;height:249px;background:linear-gradient(135deg,#2a2a2e,#dfe2e6 55%,#4a4a4a)}
.proj-b{left:477px;top:1873px;width:340px;height:249px;background:#0b2a4f}
.proj-c{left:825px;top:1873px;width:164px;height:249px;background:linear-gradient(150deg,#e7e3de,#a9714b 50%,#5e2d34)}
.start{left:0;top:2162px;width:1200px;height:380px;background:var(--dark);color:var(--paper)}
.start .section-title{top:80px;color:var(--paper)}
.start-copy{position:absolute;left:550px;top:86px;width:510px;font-size:10px;line-height:19px}
.start-copy p{margin-bottom:18px}
.footer{left:0;top:2541px;width:1200px;height:310px;background:var(--black);color:var(--paper);font-size:10px;line-height:19px}
.footer .brand{position:absolute;left:37px;top:79px;font-size:20px}
.f-col{position:absolute;top:79px}
.newsletter{position:absolute;left:932px;top:102px;width:228px;height:33px;border:1px solid #9a9a9a}
.newsletter span{position:absolute;left:12px;top:7px;color:#8a8a8a}
.newsletter .send{position:absolute;right:5px;top:6px;background:var(--paper);color:var(--ink);padding:0 9px;line-height:18px}
.f-rule{position:absolute;left:37px;top:234px;width:1126px;height:1px;background:#333}
.copyright{position:absolute;left:0;top:254px;width:1200px;text-align:center}
</style>
</head>
<body>
<header>
  <div class="abs brand" style="left:37px;top:10px">plovrak</div>
  <div class="rule" style="top:42px"></div>
</header>

<h1 class="abs headline">Plovrak builds critical applications to capture new markets, create modern services and captivate our customers in new and engaging ways.</h1>
<div class="abs side-social"><div>Friendspace</div><div>Chirpline</div><div>NetLinkPro</div></div>

<div class="photo hero-wide" role="img" aria-label="Team of four colleagues meeting around a table with laptops and plants"></div>
<div class="photo hero-low" role="img" aria-label="Continuation of the team meeting photo"></div>
<p class="abs intro">Creating effective and engaging solutions that truly work has always been Plovrak's core offering and is what makes us excited to work in digital. We are a forward thinking company embracing the opportunities of digital transformation and automations.</p>

<h2 class="section-title" style="top:955px">Services</h2>
<ul class="abs services">
  <li>Business Automation</li>
  <li>Application Development and Services for Desktop and Mobile</li>
  <li>Interface Design and UX</li>
  <li>Enterprise Integrations</li>
</ul>

<div class="rule" style="top:1254px"></div>
<h2 class="section-title" style="top:1290px">Founded by</h2>
<div class="abs founders">Torvald Bergqvist and Mikael Dahlgren</div>
<div class="abs year">in <b>2021</b></div>

<div class="rule" style="top:1454px"></div>
<h2 class="section-title" style="top:1490px">Get Connected</h2>
<div class="abs connect"><div>Friendspace</div><div>Chirpline</div><div>NetLinkPro</div></div>

<div class="rule" style="top:1660px"></div>
<h2 class="section-title" style="top:1695px">Projects</h2>
<div class="photo proj-tall" role="img" aria-label="Website project shown on a tablet against a purple backdrop"></div>
<div class="photo proj-a" role="img" aria-label="Laptop screen showing an interface design component library"></div>
<div class="photo proj-b" role="img" aria-label="Three-dimensional pink lettermark on a navy background"></div>
<div class="photo proj-c" role="img" aria-label="Students working together at a table"></div>

<section class="abs start">
  <h2 class="section-title">Let’s get started</h2>
  <div class="start-copy">
    <p>Lorem ipsum dolor sit amet, consectetuer adipiscing elit, sed diam nonummy nibh euismod tincidunt ut laoreet dolore magna aliquam erat volutpat.</p>
    <p>Ut wisi enim ad minim veniam, quis nostrud exerci tation ullamcorper suscipit lobortis nisl ut aliquip ex ea commodo consequat. Duis autem vel eum iriure dolor in hendrerit in vulputate velit esse molestie consequat, vel illum dolore eu feugiat nulla facilisis vero.</p>
    <p>Eros et accumsan et iusto odio dignissim qui blandit praesent luptatum zzril delenit augue duis dolore te feugait nulla facilisi.</p>
  </div>
</section>

<footer class="abs footer">
  <div class="brand">plovrak</div>
  <div class="f-col" style="left:246px"><div>Brunhaven , Queensland 4299, AU</div><div>555-010-2040</div></div>
  <div class="f-col" style="left:546px"><div>Friendspace</div><div>Chirpline</div><div>NetLinkPro</div></div>
  <div class="f-col" style="left:728px"><div>Privacy policy</div><div>Client login</div></div>
  <div class="f-col" style="left:932px">Subscribe to our newsletter</div>
  <div class="newsletter"><span>Your email</span><span class="send">send</span></div>
  <div class="f-rule"></div>
  <div class="copyright">©2022. plovrak.com. All Rights Reserved</div>
</footer>
</body>
</html>
```